Brixel Consulting Limited

we are a company specialising in assisting New Zealand companies to venture into China on strategy, business development, M&A, and Governance.

Industry/Entity Type

Graphic Design

```html
<!DOCTYPE html>
<html lang="en">
<head>
<meta charset="utf-8">
<title>Brixel Consulting Limited – Business Card</title>
<link rel="stylesheet" href="https://fonts.googleapis.com/css2?family=Cinzel:wght@400;700&display=swap">
<style>
  :root {
    --bg-dark: #000000;
    --bg-mid: #6a0018;
    --bg-bright: #e8002e;
    --panel: rgba(0, 0, 0, 0.32);
    --ink: #ffffff;
  }
  html, body {
    margin: 0;
    padding: 0;
    width: 1200px;
    height: 800px;
    overflow: hidden;
    background: #ffffff;
  }
  .card {
    position: relative;
    width: 1200px;
    height: 800px;
    overflow: hidden;
    background: linear-gradient(145deg, var(--bg-dark) 0%, #2a0008 30%, var(--bg-mid) 62%, var(--bg-bright) 100%);
    font-family: "Cinzel", "Trajan Pro", serif;
    color: var(--ink);
  }
  .card__panel {
    position: absolute;
    left: 43px;
    top: 37px;
    width: 1114px;
    height: 723px;
    background: var(--panel);
  }
  .company-name {
    position: absolute;
    top: 92px;
    left: 0;
    width: 100%;
    margin: 0;
    text-align: center;
    font-size: 28px;
    font-weight: 400;
    letter-spacing: 1px;
  }
  .person {
    position: absolute;
    top: 348px;
    left: 134px;
    width: 931px;
    text-align: center;
  }
  .person__name {
    margin: 0;
    font-size: 44px;
    font-weight: 400;
    line-height: 50px;
    letter-spacing: 1px;
  }
  .person__rule {
    display: block;
    width: 100%;
    height: 2px;
    background: var(--ink);
    margin: 0;
  }
  .person__title {
    margin: 4px 0 0;
    font-size: 21px;
    font-weight: 700;
    letter-spacing: 1.5px;
    line-height: 26px;
  }
  .contact {
    position: absolute;
    left: 64px;
    top: 646px;
    margin: 0;
    padding: 0;
    list-style: none;
    font-size: 27px;
    line-height: 35px;
    letter-spacing: 0.5px;
  }
</style>
</head>
<body>
  <div class="card">
    <div class="card__panel"></div>
    <h1 class="company-name">Brixel Consulting Limited</h1>
    <div class="person">
      <h2 class="person__name">Mara-Li Chen</h2>
      <span class="person__rule"></span>
      <p class="person__title">managing director</p>
    </div>
    <ul class="contact">
      <li class="contact__item">Phone: +64 21 555 0147</li>
      <li class="contact__item">Skype:maralichenbrixel</li>
      <li class="contact__item">email: mara-li.chen@brixelconsulting.com</li>
    </ul>
  </div>
</body>
</html>
```